Penny auctions banner design to get people to sign up

Show the 3 steps needed to get started bidding with penny auctions on my website Vornek.com. The core colors should be black, grey, and yellow.

It needs to show the following steps: 1) Register an account. 2) Purchase the starter package. 3) Start bidding and save up to 98% off!

Some creativity would be good so if you have some better ideas then please let them flow and show me your best banner design :) Thank you! Comment with any questions you have. Attached is my logo.

```html
<!DOCTYPE html>
<html lang="en">
<head>
<meta charset="utf-8">
<title>Vornek – Get Started Banner Slides</title>
<link href="https://fonts.googleapis.com/css2?family=Ubuntu:wght@500;700&display=swap" rel="stylesheet">
<style>
  :root {
    --page-bg: #f3f3f3;
    --page-bg-edge: #e6e6e6;
    --dark: #1c1c1c;
    --dark-2: #2a2a2a;
    --panel-light: #ffffff;
    --panel-shade: #d9d9d9;
    --yellow: #ffc619;
    --yellow-deep: #f2a900;
    --ink: #1a1a1a;
    --accent-red: #d8341c;
  }
  * { box-sizing: border-box; margin: 0; padding: 0; }
  html, body {
    width: 1200px; height: 773px; overflow: hidden;
  }
  body {
    position: relative;
    background: radial-gradient(ellipse at 50% 45%, var(--page-bg) 55%, var(--page-bg-edge) 100%);
    font-family: "Ubuntu", sans-serif;
    color: var(--ink);
  }
  .slide {
    position: absolute;
    left: 216px;
    width: 768px;
    height: 187px;
    overflow: hidden;
  }
  .slide--one { top: 28px; }
  .slide--two { top: 231px; }
  .slide--three { top: 435px; }
  .slide__art { position: absolute; inset: 0; width: 768px; height: 187px; }
  .step-badge {
    position: absolute;
    left: 276px;
    width: 72px; height: 72px;
    border-radius: 50%;
    background: radial-gradient(circle at 40% 35%, #ffffff 55%, #e4e4e4 100%);
    border: 4px solid var(--ink);
    box-shadow: 0 2px 4px rgba(0,0,0,.25);
    display: flex; align-items: center; justify-content: center;
    font-weight: 700; font-size: 50px; line-height: 1;
    color: var(--yellow);
    -webkit-text-stroke: 1.5px var(--yellow-deep);
  }
  .slide--one .step-badge { top: 5px; }
  .slide--two .step-badge,
  .slide--three .step-badge { top: 20px; }
  .step-text {
    position: absolute;
    left: 112px; width: 400px;
    text-align: center;
    font-weight: 700;
    text-transform: uppercase;
    color: var(--ink);
    letter-spacing: .5px;
  }
  .slide--one .step-text { top: 128px; font-size: 33px; line-height: 1; }
  .slide--two .step-text,
  .slide--three .step-text { top: 102px; font-size: 31px; line-height: 40px; }
  .step-text .highlight { color: var(--accent-red); }
  .brand {
    position: absolute;
    left: 628px; width: 121px;
    top: 18px;
    display: flex; flex-direction: column; align-items: center;
  }
  .brand__dot {
    width: 30px; height: 30px; border-radius: 50%;
    background: var(--yellow);
    margin-bottom: 6px;
  }
  .brand__name {
    font-weight: 700; font-size: 26px; line-height: 1;
    color: var(--yellow);
  }
  .go-button {
    position: absolute;
    left: 628px; top: 122px;
    width: 121px; height: 46px;
    border-radius: 23px;
    background: linear-gradient(#ffe15a, var(--yellow) 50%, var(--yellow-deep));
    border: 2px solid #8a6200;
    display: flex; align-items: center; justify-content: center; gap: 8px;
    font-weight: 700; font-size: 28px; color: var(--ink);
  }
  .go-button svg { width: 16px; height: 20px; }
  .caption {
    position: absolute; left: 0; width: 1200px; text-align: center;
    font-weight: 700; color: var(--ink);
  }
  .caption--main { top: 648px; font-size: 47px; }
  .caption--sub { top: 708px; font-size: 29px; font-weight: 500; }
</style>
</head>
<body>

<svg width="0" height="0" style="position:absolute">
  <defs>
    <radialGradient id="panel-fill" cx="45%" cy="40%" r="65%">
      <stop offset="0%" stop-color="#ffffff"/>
      <stop offset="70%" stop-color="#ececec"/>
      <stop offset="100%" stop-color="#d4d4d4"/>
    </radialGradient>
    <linearGradient id="dark-fill" x1="0" y1="0" x2="0" y2="1">
      <stop offset="0%" stop-color="#262626"/>
      <stop offset="100%" stop-color="#141414"/>
    </linearGradient>
    <symbol id="slide-frame" viewBox="0 0 768 187">
      <rect width="768" height="187" fill="url(#dark-fill)"/>
      <path d="M44,0 Q-14,93.5 44,187 L598,187 Q652,93.5 598,0 Z" fill="url(#panel-fill)"/>
      <path d="M40,-2 Q-20,93.5 40,189" fill="none" stroke="#ffc619" stroke-width="9"/>
    </symbol>
  </defs>
</svg>

<section class="slide slide--one">
  <svg class="slide__art" viewBox="0 0 768 187" aria-hidden="true"><use href="#slide-frame"/></svg>
  <div class="step-badge">1</div>
  <p class="step-text">Register an account</p>
  <div class="brand"><span class="brand__dot"></span><span class="brand__name">Vornek</span></div>
  <div class="go-button">GO<svg viewBox="0 0 16 20"><path d="M0,0 L16,10 L0,20 Z" fill="#1a1a1a"/></svg></div>
</section>

<section class="slide slide--two">
  <svg class="slide__art" viewBox="0 0 768 187" aria-hidden="true"><use href="#slide-frame"/></svg>
  <div class="step-badge">2</div>
  <p class="step-text">Purchase the<br>starter package.</p>
  <div class="brand"><span class="brand__dot"></span><span class="brand__name">Vornek</span></div>
  <div class="go-button">GO<svg viewBox="0 0 16 20"><path d="M0,0 L16,10 L0,20 Z" fill="#1a1a1a"/></svg></div>
</section>

<section class="slide slide--three">
  <svg class="slide__art" viewBox="0 0 768 187" aria-hidden="true"><use href="#slide-frame"/></svg>
  <div class="step-badge">3</div>
  <p class="step-text">Start bidding and<br>save up to <span class="highlight">98%</span> off!</p>
  <div class="brand"><span class="brand__dot"></span><span class="brand__name">Vornek</span></div>
  <div class="go-button">GO<svg viewBox="0 0 16 20"><path d="M0,0 L16,10 L0,20 Z" fill="#1a1a1a"/></svg></div>
</section>

<p class="caption caption--main">Those are 3 slides of an animated banner.</p>
<p class="caption caption--sub">Please check the link in the description to view the animation.</p>

</body>
</html>
```